Change English consent to translated Arabic and Persian on adobe indesign.

I need two consent forms done.
First one needs English replaced wiht arabic
Second one needs English replaced with persian

I will send the indesign once you accept the project as the file is large.
I have attached the translation.
No real graphics need to be done.

Please get Adobe Indesign file from this link
https://sendbundle.net/274619083

The translations are attached to this project.

```html
<!DOCTYPE html>
<html lang="fa" dir="rtl">
<head>
<meta charset="utf-8">
<title>فرم رضایت بیمار</title>
<link href="https://fonts.googleapis.com/css2?family=Vazirmatn:wght@400;500;700;900&display=swap" rel="stylesheet">
<style>
:root{
  --brand:#1a9ad6;
  --band-light:#5fc3e8;
  --band-dark:#1f8ccc;
  --ink:#1e5f9c;
  --ink-soft:#3a78b3;
  --rule:#9bbad6;
  --paper:#ffffff;
}
*{box-sizing:border-box;margin:0;padding:0}
html,body{width:848px;height:1200px;overflow:hidden;background:var(--paper)}
body{font-family:"Vazirmatn",sans-serif;color:var(--ink);position:relative}
.abs{position:absolute}
.brand{left:78px;top:30px;direction:ltr;font-weight:900;font-size:56px;line-height:1;color:var(--brand)}
.band{left:0;width:848px;color:#fff;font-weight:900;text-align:center;display:flex;align-items:center;justify-content:center}
.band-title{top:116px;height:34px;background:var(--brand);font-size:18px}
.band-title .latin{font-weight:400}
.band-sub{top:150px;height:32px;background:var(--band-light);font-size:20px}
.sec-head{font-weight:900;font-size:17px;color:var(--ink)}
.rule{height:0;border-top:1.5px solid var(--ink)}
.rule.soft{border-top:1px solid var(--rule)}
.field{display:flex;align-items:flex-end;gap:4px;font-size:10.5px;font-weight:700;height:16px}
.field .line{flex:1;border-bottom:1px solid var(--ink-soft);height:10px}
.col-r{right:52px;width:394px}
.col-l{right:482px;width:330px}
.box{display:inline-block;width:16px;height:16px;border:1.3px solid var(--ink);flex:none}
.row{display:flex;align-items:center;gap:8px;font-size:12.5px;right:52px;left:70px}
.row.small{font-size:10.5px;font-weight:700;gap:6px}
.h2{font-weight:900;font-size:21px;right:52px}
.h2 span{font-weight:400}
.q{right:52px;font-size:12.5px}
.yn{display:flex;align-items:center;gap:8px;font-size:12.5px}
.cert{right:52px;left:44px;font-size:11px;font-weight:700}
.cert li{margin-right:18px;margin-bottom:5px}
.para{right:52px;left:54px;font-size:10.5px;line-height:21.5px;color:var(--ink-soft)}
.sign{font-size:12.5px;font-weight:700}
.footer{left:0;top:1172px;width:848px;height:28px;background:var(--band-dark);color:#fff;font-size:10.5px;display:flex;justify-content:space-between;align-items:center;padding:0 52px 0 92px}
</style>
</head>
<body>
<div class="abs brand">Nirova</div>

<div class="abs band band-title">فرم رضایت بیمار از امکان پرداخت&nbsp;<span class="latin">Bulk billing</span>&nbsp;در برنامه خدمات دندان‌پزشکی کودکان</div>
<div class="abs band band-sub">تمام اطلاعات شما محرمانه خواهند ماند.</div>

<div class="abs sec-head" style="right:52px;top:194px">اطلاعات بیمار</div>
<div class="abs sec-head" style="right:482px;top:194px">شماره واحه</div>
<div class="abs rule" style="right:52px;left:36px;top:215px"></div>

<div class="abs col-r" style="top:222px"><div class="field"><span>نام (نامها):</span><span class="line"></span></div></div>
<div class="abs col-r" style="top:244px"><div class="field"><span>تاریخ تولد:</span><span class="line"></span></div></div>
<div class="abs col-r" style="top:265px"><div class="field"><span>حضور غیاب در کلاس:</span><span class="line"></span></div></div>
<div class="abs col-r" style="top:287px"><div class="field"><span>جنسیت: مرد/زن</span><span class="line"></span></div></div>
<div class="abs col-r" style="top:308px"><div class="field"><span>شماره تلفن (منزل):</span><span class="line"></span></div></div>
<div class="abs col-r" style="top:330px"><div class="field"><span>شماره تلفن (محل کار):</span><span class="line"></span></div></div>
<div class="abs col-r" style="top:351px"><div class="field"><span>شماره همراه:</span><span class="line"></span></div></div>
<div class="abs col-r" style="top:373px"><div class="field"><span>شماره ارجاع:</span><span class="line"></span></div></div>

<div class="abs col-l" style="top:222px"><div class="field"><span>نام خانوادگی:</span><span class="line"></span></div></div>
<div class="abs col-l" style="top:244px"><div class="field"><span>نام مدرسه:</span><span class="line"></span></div></div>
<div class="abs col-l" style="top:265px"><div class="field"><span>نام ولی/ سرپرست قانونی:</span><span class="line"></span></div></div>
<div class="abs col-l" style="top:287px"><div class="field"><span>آدرس:</span><span class="line"></span></div></div>
<div class="abs col-l" style="top:308px"><div class="field"><span>حاشیه شهر:</span><span class="line"></span></div></div>
<div class="abs col-l" style="top:330px"><div class="field"><span>کد پستی:</span><span class="line"></span></div></div>
<div class="abs col-l" style="top:351px"><div class="field"><span>ایمیل:</span><span class="line"></span></div></div>
<div class="abs col-l" style="top:373px"><div class="field"><span>شماره کارت PublicCare:</span><span class="line"></span></div></div>

<div class="abs row small" style="top:401px;left:64px">
  <span>آیا از بومیان استرالیایی هستید یا بومی جزایر Torres Strait هستید</span>
  <span style="flex:1"></span>
  <span class="box"></span><span>بله از بومیان استرالیا هستم.</span>
  <span class="box"></span><span>بله از بومیان جزایر Torres Strait هستم.</span>
  <span class="box"></span><span>خیر</span>
</div>
<div class="abs rule soft" style="right:36px;left:36px;top:424px;border-color:var(--ink-soft)"></div>

<div class="abs h2" style="top:426px">در صورت موافقت، تیک بزنید<span>.</span></div>
<div class="abs row" style="top:460px;align-items:flex-start"><span class="box" style="margin-top:4px"></span><span style="line-height:21px">رضایت خود را برای معالجه رایگان دندان‌پزشکی به‌وسیله Nirova اعلام می‌کنم (اگر نیاز به اشعه ایکس باشد، به صورت bulk bill از طریق Nirova پرداخت می‌شود).</span></div>
<div class="abs row" style="top:509px"><span class="box"></span><span>رضایت خود را برای انجام معاینه، جرم‌گیری، پاک کردن و درمان فلوراید و اشعه ایکس که توسط Nirova انجام می‌شود، اعلام می‌کنم.</span></div>
<div class="abs row" style="top:540px"><span class="box"></span><span>نمی‌خواهم فرزندم در برنامه دندان‌پزشکی شرکت کند.</span></div>
<div class="abs rule soft" style="right:36px;left:36px;top:584px;border-color:var(--ink-soft)"></div>

<div class="abs h2" style="top:590px">در صورت موافقت، تیک بزنید<span>.</span></div>
<div class="abs row" style="top:625px"><span class="box"></span><span>فرزند من برای برنامه KDSP واجد شرایط است.</span></div>
<div class="abs row" style="top:652px"><span class="box"></span><span>مطمئن نیستم فرزندم برای برنامه KDSP واجدالشرایط باشد؛ لطفاً از طرف من این قضیه را با PublicCare بررسی کنید.</span></div>
<div class="abs row" style="top:678px"><span class="box"></span><span>رضایت می دهم اگر فرزندم به درمان بیشتری نیاز داشت با تلفن خبرم کنید.</span></div>
<div class="abs rule soft" style="right:44px;left:44px;top:708px;border-color:var(--ink-soft)"></div>

<div class="abs h2" style="top:714px">لطفا کامل کنید<span>.</span></div>
<div class="abs q" style="top:752px">آخرین باری که یک دندان‌پزشک فرزندتان را ویزیت کرد، کِی بود؟</div>
<div class="abs q" style="top:779px">آخرین باری که برای دندان های فرزندتان از اشعه ایکس استفاده شد، چه زمان بود؟</div>

<div class="abs q" style="top:806px">وضعیت سلامتی (مثلاً بیماری قلبی)</div>
<div class="abs yn" style="right:308px;top:806px"><span>خیر</span><span class="box"></span><span style="width:22px"></span><span class="box"></span><span>بله</span></div>
<div class="abs q" style="right:564px;top:806px">(لطفاً جزییات را قید کنید)</div>
<div class="abs rule soft" style="right:44px;left:44px;top:850px"></div>

<div class="abs q" style="top:860px">دارو مثل والپروات سدیم</div>
<div class="abs yn" style="right:308px;top:860px"><span>خیر</span><span class="box"></span><span style="width:22px"></span><span class="box"></span><span>بله</span></div>
<div class="abs q" style="right:564px;top:860px">(لطفاً جزییات را قید کنید)</div>
<div class="abs rule soft" style="right:44px;left:44px;top:894px"></div>

<div class="abs q" style="top:905px">آلرژی‌زا مانند پنی‌سیلین</div>
<div class="abs yn" style="right:308px;top:905px"><span>خیر</span><span class="box"></span><span style="width:22px"></span><span class="box"></span><span>بله</span></div>
<div class="abs q" style="right:564px;top:905px">(لطفاً جزییات را قید کنید)</div>
<div class="abs rule soft" style="right:44px;left:44px;top:938px"></div>

<div class="abs cert" style="top:942px">
  <p style="font-size:12px;margin-bottom:6px">من به عنوان ولی/ سرپرست قانونی گواهی می دهم که از موارد زیر مطلع شده ام:</p>
  <ul>
    <li>درمان تحت برنامه مزایای دندان‌پزشکی کودک از این تاریخ شروع شده یا شروع خواهد شد.</li>
    <li>هزینه‌های احتمالی این درمان و اینکه برای خدمات برنامه مزایای دندان‌پزشکی کودک از Bulk billing استفاده خواهد شد.</li>
    <li>اینکه برای این خدمات، بابت هزینه‌های پیش‌بینی‌نشده پول نخواهم داد؛ اعتبار مالی کافی برای این خدمات در برنامه مزایای دندان‌پزشکی کودک لحاظ شده است.</li>
  </ul>
</div>

<p class="abs para" style="top:1034px">می‌دانم که من/بیمار تنها به آن دسته از مزایای دندان‌پزشکی که در محدوده برنامه خدمات دندان‌پزشکی کودکان هستند، دسترسی دارم. می‌فهمم که مزایای برخی از خدمات با محدودیت روبرو هستند و برنامه مزایای خدمات دندان‌پزشکی کودکان شامل تعداد محدودی از خدمات است. متوجه هستم که هزینه خدماتی را که تحت پوشش این برنامه نیستند، باید شخصاً بپردازم. می‌دانم که هزینه خدمات، حد مزایای موجود را کاهش می‌دهد و در صورت تمام شدن مزایا، باید شخصاً هزینه خدمات اضافی را بپردازم.</p>

<div class="abs rule soft" style="right:44px;left:44px;top:1112px"></div>
<div class="abs sign" style="right:52px;top:1116px">امضای بیمار/سرپرست قانونی</div>
<div class="abs rule soft" style="right:208px;left:298px;top:1133px;border-color:var(--ink-soft)"></div>
<div class="abs sign" style="right:616px;top:1116px">تاریخ</div>
<div class="abs rule soft" style="right:656px;left:44px;top:1133px;border-color:var(--ink-soft)"></div>
<div class="abs sign" style="right:52px;top:1144px">نام کامل امضاکننده (در صورتی که بیمار امضا نکند)</div>
<div class="abs rule soft" style="right:328px;left:44px;top:1161px;border-color:var(--ink-soft)"></div>

<div class="abs footer"><span>این فرم تا ۳۱ دسامبر اعتبار دارد</span><span>به‌روزرسانی: ترم اول سال ۲۰۱۶</span></div>
</body>
</html>
```